Sheriff Candidate needs a large yard sign

A candidate for Sheriff needs to have a sign to put in front of businesses and houses that advertise her candidacy.

Target Market(s)

Democrats, voters

Industry/Entity Type

Political

Font styles to use
Sans Serif

Colors
34a7d7
3276b5

Requirements
Must have
• Must have her picture
• Must have the words "Elect Dana Holloway" - I'd like the name Dana to be smaller Holloway. "Elect" and "Holloway" should be the focus.
• at the bottom in a box "Paid for by the Committee to Elect Dana Holloway"
Nice to have
• it would be good to have her logo as well.
• blue color for democrats and on a white background
Should not have
• pink color

```html
<!DOCTYPE html>
<html lang="en">
<head>
<meta charset="utf-8">
<title>Elect Dana Holloway – Yard Sign</title>
<link rel="stylesheet" href="https://fonts.googleapis.com/css2?family=Open+Sans:wght@600&family=Alfa+Slab+One&family=Oswald:wght@400&display=swap">
<style>
  :root {
    --backdrop: #c3c4c7;
    --sign-light: #ffffff;
    --sign-grey: #d9dadc;
    --ink-dark: #3c3e3e;
    --ink-soft: #a8a9ab;
    --party-blue: #2176b9;
    --accent-blue: #3276b5;
    --footer-navy: #1f2439;
    --footer-text: #a7abbd;
    --photo-dark: #22273a;
    --photo-mid: #3a3f52;
  }
  * { margin: 0; padding: 0; box-sizing: border-box; }
  html, body { width: 1200px; height: 1000px; overflow: hidden; }
  body { background: var(--backdrop); position: relative; }

  .yard-sign {
    position: absolute; left: 32px; top: 165px;
    width: 1133px; height: 665px;
    background: linear-gradient(90deg, var(--sign-light) 0%, #eeeff0 45%, var(--sign-grey) 100%);
    overflow: hidden;
  }
  .candidate-photo {
    position: absolute; left: 0; top: 10px;
    width: 388px; height: 530px;
    background: radial-gradient(ellipse at 50% 70%, var(--photo-mid) 0%, var(--photo-dark) 60%, rgba(34,39,58,0.9) 100%);
    border-radius: 160px 160px 0 0;
  }
  .headline {
    position: absolute; left: 418px; top: 40px;
    font-family: "Open Sans", sans-serif; font-weight: 600;
    font-size: 238px; line-height: 1; color: var(--ink-dark);
    letter-spacing: 2px;
  }
  .first-name {
    position: absolute; left: 428px; top: 290px;
    font-family: "Open Sans", sans-serif; font-weight: 600;
    font-size: 58px; line-height: 1; color: var(--ink-soft);
  }
  .last-name {
    position: absolute; left: 424px; top: 338px;
    font-family: "Alfa Slab One", serif;
    font-size: 108px; line-height: 1.1; color: var(--party-blue);
    letter-spacing: 1px;
    -webkit-text-stroke: 3px #ffffff; paint-order: stroke fill;
  }
  .accent-stripe {
    position: absolute; left: 0; top: 527px; width: 1133px; height: 14px;
  }
  .disclaimer-band {
    position: absolute; left: 0; top: 540px; width: 1133px; height: 125px;
    background: var(--footer-navy);
  }
  .disclaimer {
    position: absolute; left: 60px; top: 28px;
    font-family: "Oswald", sans-serif; font-weight: 400;
    font-size: 46px; line-height: 1.3; color: var(--footer-text);
  }
  .campaign-mark {
    position: absolute; left: 968px; top: 34px;
    display: flex; align-items: center; gap: 10px;
  }
  .campaign-mark-dot {
    width: 22px; height: 22px; border-radius: 50%; background: var(--accent-blue);
  }
  .campaign-mark-name {
    font-family: "Oswald", sans-serif; font-weight: 400;
    font-size: 22px; line-height: 1.15; color: var(--footer-text);
  }
</style>
</head>
<body>
  <div class="yard-sign">
    <div class="candidate-photo" role="img" aria-label="Portrait photo of the candidate in a dark blazer"></div>
    <div class="headline">ELECT</div>
    <div class="first-name">DANA</div>
    <div class="last-name">HOLLOWAY</div>
    <svg class="accent-stripe" viewBox="0 0 1133 14" preserveAspectRatio="none">
      <polygon points="190,0 1133,0 1133,14 175,14" fill="var(--party-blue)"/>
    </svg>
    <div class="disclaimer-band">
      <p class="disclaimer">Paid for by the Committee to Elect Dana Holloway</p>
      <div class="campaign-mark">
        <span class="campaign-mark-dot"></span>
        <span class="campaign-mark-name">Holloway<br>for Sheriff</span>
      </div>
    </div>
  </div>
</body>
</html>
```